Sunny Ladle Kitchen April Competition

The website slider is 990 X 225 pixels to fit in with this website www.sunnyladlekitchen.com.au

We would love a fun, lively, food-oriented slider created for Sunny Ladle Kitchen website. Sunny Ladle Kitchen is a central place where people who love food, cooking for their family and friends, and sharing recipes can hang out. We'd like the sliders to be simple, bright and to entice people to click on the link.

The banner ad needs to feature the Coastal Readers' Monthly cookbooks, and to use a colour scheme that also works with the existing website.

A slider in March was used to promote a similar competition which I will upload as inspiration, along with the image of the cook books to use.

Main text: Add your best mid-week meal recipes to win one of 8 cookbook sets!
Smaller text: The 8 best recipes as chosen by Sunny Ladle Kitchen editors will win.

```html
<!DOCTYPE html>
<html lang="en">
<head>
<meta charset="utf-8">
<title>Sunny Ladle Kitchen April Competition</title>
<link rel="stylesheet" href="https://fonts.googleapis.com/css2?family=Cinzel:wght@600&family=Fraunces:wght@500&family=Open+Sans:wght@400;700&display=swap">
<style>
  :root {
    --brown-light: #84401f;
    --brown-mid: #66301a;
    --brown-dark: #3f190b;
    --wood-light: #b8804c;
    --wood-dark: #7a4a26;
    --cream-gold: #f7e4a2;
    --cream: #fbf1d6;
    --white: #ffffff;
    --badge-orange: #f28a1e;
    --badge-orange-deep: #e06d10;
  }
  * { margin: 0; padding: 0; box-sizing: border-box; }
  html, body {
    width: 1200px;
    height: 274px;
    overflow: hidden;
    background: var(--brown-dark);
  }
  .slider {
    position: relative;
    width: 1200px;
    height: 274px;
    overflow: hidden;
    background: radial-gradient(ellipse at 60% 30%, var(--brown-light) 0%, var(--brown-mid) 50%, var(--brown-dark) 100%);
  }
  .showcase {
    position: absolute;
    left: 0;
    top: 0;
    width: 460px;
    height: 274px;
  }
  .headline-kicker,
  .headline-main,
  .prize,
  .judging-note {
    position: absolute;
    text-align: center;
    white-space: nowrap;
    line-height: 1;
  }
  .headline-kicker,
  .headline-main {
    font-family: "Cinzel", serif;
    font-weight: 600;
    color: var(--cream-gold);
    text-shadow: 0 2px 3px rgba(0, 0, 0, 0.45);
  }
  .headline-kicker {
    left: 725px;
    width: 400px;
    top: 10px;
    font-size: 48px;
  }
  .headline-main {
    left: 489px;
    width: 700px;
    top: 56px;
    font-size: 52px;
    letter-spacing: -0.5px;
  }
  .prize {
    font-family: "Fraunces", serif;
    font-weight: 500;
    color: var(--cream);
    font-size: 64px;
    letter-spacing: 1.5px;
    text-shadow: 0 2px 3px rgba(0, 0, 0, 0.5);
  }
  .prize-line-one { left: 518px; width: 600px; top: 106px; }
  .prize-line-two { left: 497px; width: 600px; top: 167px; }
  .judging-note {
    left: 441px;
    top: 243px;
    width: 760px;
    font-family: "Open Sans", sans-serif;
    font-size: 19px;
    color: var(--white);
  }
  .cta-badge {
    position: absolute;
    left: 1075px;
    top: 120px;
    width: 88px;
    height: 86px;
    text-decoration: none;
  }
  .cta-badge svg {
    position: absolute;
    inset: 0;
    width: 100%;
    height: 100%;
  }
  .cta-label {
    position: absolute;
    inset: 0;
    display: flex;
    align-items: center;
    justify-content: center;
    text-align: center;
    font-family: "Open Sans", sans-serif;
    font-weight: 700;
    font-size: 11px;
    line-height: 1.1;
    color: var(--white);
  }
</style>
</head>
<body>
  <main class="slider">
    <svg class="showcase" viewBox="0 0 460 274" role="img" aria-label="Wooden tabletop with three fanned-out Coastal Readers' Monthly cookbooks">
      <defs>
        <linearGradient id="wood-tone" x1="0" y1="0" x2="1" y2="1">
          <stop offset="0" stop-color="var(--wood-light)"/>
          <stop offset="1" stop-color="var(--wood-dark)"/>
        </linearGradient>
      </defs>
      <polygon points="0,0 370,0 442,137 370,274 0,274" fill="url(#wood-tone)"/>
      <polyline points="370,0 442,137 370,274" fill="none" stroke="var(--cream)" stroke-width="3" stroke-opacity="0.85"/>
      <polyline points="382,0 454,137 382,274" fill="none" stroke="var(--cream)" stroke-width="1" stroke-opacity="0.35"/>
    </svg>

    <h1>
      <span class="headline-kicker">ADD YOUR BEST</span>
      <span class="headline-main">MID-WEEK MEAL RECIPES</span>
      <span class="prize prize-line-one">to Win One of</span>
      <span class="prize prize-line-two">8 Cookbook Sets!</span>
    </h1>

    <a class="cta-badge" href="#">
      <svg viewBox="0 0 100 96" aria-hidden="true">
        <polygon fill="var(--badge-orange)" stroke="var(--badge-orange-deep)" stroke-width="1"
          points="50,2 59,16 75,8 76,25 94,26 86,42 98,54 83,62 88,80 71,79 64,94 50,84 36,94 29,79 12,80 17,62 2,54 14,42 6,26 24,25 25,8 41,16"/>
      </svg>
      <span class="cta-label">FIND OUT<br>MORE<br>HERE</span>
    </a>

    <p class="judging-note">THE 8 BEST RECIPES AS CHOSEN BY SUNNY LADLE KITCHEN EDITORS WILL WIN</p>
  </main>
</body>
</html>
```